Varlo Building Pty Ltd need an Identity!

We need a logo design for a building company based in Sydney, Australia. In addition - Business Card Layout. The colour scheme is to be black and red and communicate a professional yet 'hands on' approach to building.

Target Market(s)

Architects, Home Owners, Developers

Industry/Entity Type

Construction

Font styles to use
Serif
Sans Serif

Colors
ec1f27

Requirements
Must have
• Clear logo and professional direction.
Nice to have
• Use of initials as a possible logo
Should not have
• Graphics/pictures of houses, house roofs etc. Can be an abstracted form of a building.

```html
<!DOCTYPE html>
<html lang="en">
<head>
<meta charset="utf-8">
<title>Varlo Building Pty Ltd – Identity</title>
<link rel="stylesheet" href="https://fonts.googleapis.com/css2?family=PT+Sans+Narrow:wght@400;700&family=Roboto+Condensed:wght@700&display=swap">
<style>
  :root {
    --brand-red: #e04438;
    --ink: #111111;
    --steel: #808285;
    --paper: #ffffff;
    --card-edge: #c8c8c8;
  }
  html, body {
    margin: 0;
    padding: 0;
    width: 1200px;
    height: 1200px;
    overflow: hidden;
    background: var(--paper);
  }
  .sheet {
    position: relative;
    width: 1200px;
    height: 1200px;
    font-family: "PT Sans Narrow", "Arial Narrow", sans-serif;
    color: var(--ink);
  }

  /* Wordmark lockups */
  .wordmark {
    position: absolute;
    display: flex;
    align-items: center;
    justify-content: center;
    gap: 16px;
    font-family: "PT Sans Narrow", "Arial Narrow", sans-serif;
    font-weight: 700;
    letter-spacing: 0.02em;
    line-height: 1;
  }
  .wordmark__square {
    display: block;
    flex: none;
  }
  .wordmark--primary { left: 228px; top: 76px; width: 260px; height: 178px; font-size: 78px; color: var(--ink); }
  .wordmark--primary .wordmark__square { width: 44px; height: 44px; background: var(--brand-red); }
  .wordmark--mono { left: 698px; top: 76px; width: 254px; height: 178px; font-size: 78px; color: var(--ink); }
  .wordmark--mono .wordmark__square { width: 44px; height: 44px; background: var(--steel); }

  /* Business cards */
  .card {
    position: absolute;
    width: 446px;
    height: 282px;
    box-sizing: border-box;
  }
  .card--outlined { border: 1px solid var(--card-edge); background: var(--paper); }
  .card--red-front { left: 133px; top: 421px; background: var(--brand-red); }
  .card--back-a { left: 616px; top: 421px; }
  .card--white-front { left: 131px; top: 782px; }
  .card--back-b { left: 616px; top: 782px; }

  .card--red-front .wordmark { inset: 0; font-size: 80px; color: var(--paper); }
  .card--red-front .wordmark__square { width: 46px; height: 46px; background: var(--paper); }

  .card--white-front .wordmark { left: 0; right: 0; top: 62px; height: 100px; font-size: 62px; color: var(--brand-red); gap: 12px; }
  .card--white-front .wordmark__square { width: 36px; height: 36px; background: var(--brand-red); }
  .company-caption {
    position: absolute;
    left: 0; right: 0;
    top: 172px;
    text-align: center;
    font-family: "Roboto Condensed", "Arial Narrow", sans-serif;
    font-weight: 700;
    font-size: 22px;
    letter-spacing: 0.01em;
    color: var(--ink);
  }

  /* Contact text blocks */
  .text-block {
    position: absolute;
    margin: 0;
    font-size: 16px;
    line-height: 22.5px;
  }
  .text-block strong { font-weight: 700; }
  .text-block--right { text-align: right; }
  .person-name { color: var(--brand-red); font-weight: 700; display: block; }
  .person-role { color: var(--brand-red); display: block; }
  .divider {
    position: absolute;
    width: 1px;
    background: #555;
  }

  .card--back-a .company-block { right: 213px; top: 47px; }
  .card--back-a .divider { left: 246px; top: 51px; height: 110px; }
  .card--back-a .contact-block { right: 213px; top: 191px; }
  .card--back-a .person-block { left: 246px; top: 191px; }

  .card--back-b .person-block { left: 54px; top: 60px; }
  .card--back-b .contact-block { left: 217px; top: 63px; }
  .card--back-b .company-block { left: 217px; top: 139px; }
</style>
</head>
<body>
<main class="sheet">

  <div class="wordmark wordmark--primary" aria-label="Varlo wordmark, colour">
    <span class="wordmark__square"></span>VARLO
  </div>
  <div class="wordmark wordmark--mono" aria-label="Varlo wordmark, greyscale">
    <span class="wordmark__square"></span>VARLO
  </div>

  <section class="card card--red-front" aria-label="Business card front, red">
    <div class="wordmark"><span class="wordmark__square"></span>VARLO</div>
  </section>

  <section class="card card--outlined card--back-a" aria-label="Business card back, version one">
    <p class="text-block text-block--right company-block">
      <strong>Varlo Building Pty Ltd</strong><br>
      Calder Street 118<br>
      11302 Sydney, Australia<br>
      www.varlobuilding.au
    </p>
    <span class="divider"></span>
    <p class="text-block text-block--right contact-block">
      <strong>M</strong> +61 34 111 222<br>
      <strong>E</strong> daniel@varlobuilding.au
    </p>
    <p class="text-block person-block">
      <span class="person-name">Daniel Surname</span>
      <span class="person-role">Manager Construction</span>
    </p>
  </section>

  <section class="card card--outlined card--white-front" aria-label="Business card front, white">
    <div class="wordmark"><span class="wordmark__square"></span>VARLO</div>
    <div class="company-caption">VARLO BUILDING PTY LTD</div>
  </section>

  <section class="card card--outlined card--back-b" aria-label="Business card back, version two">
    <p class="text-block person-block">
      <span class="person-name">Daniel Surname</span>
      <span class="person-role">Manager Construction</span>
    </p>
    <p class="text-block contact-block">
      <strong>M</strong> +61 34 111 222<br>
      <strong>E</strong> daniel@varlobuilding.au
    </p>
    <p class="text-block company-block">
      <strong>Varlo Building Pty Ltd</strong><br>
      Calder Street 118<br>
      11302 Sydney, Australia<br>
      www.varlobuilding.au
    </p>
  </section>

</main>
</body>
</html>
```